Children’s entertainer/balloon artist Website Home Page and custom landing page

I need a home page design for the home page of a children and family entertainer/balloon twister’s website. I also need a custom landing page for family theatre shows performed by the same entertainer.
It will be a Wordpress website and I need the final artwork in a layer Photoshop file with all the layers clearly named and labeled.

Target Market(s)

The site visitors are mainly mums, aged between early 20’s and late 30’s. Other visitors will included companies for Christmas functions, and event organisers for corporate functions.

Industry/Entity Type

Entertainment

Number of Pages Required

2 page

Font styles to use
Sans Serif

Colors
34a6d7
f37122

Requirements
Must have
• Layout
• I have included a wireframe for the home page layout and the custom landing page for your reference. This is a guide only and I welcome your interpretation with the rough layout provided.
• This website needs to look good on all devices as it will be fully responsive.
• It needs to include a footer area on the page, that has social media and a call to action area included.
• Colours
• The main colours for the site is:
• orange (call to action colour)
• ff6800
• blue/turquoise
• 42abc3
• Pictures
• I have included images of the entertainer/balloon artist for you to use/take inspiration from.
• These images will be included on the website. I want to show lots of people having fun.
• I would like to have elements of the logo used in isolation across the website
• i.e. the octopus figure to be included in the footer or the bird element to be included in the testimonial slider etc.
• Elements to include
• Note: use the images of the entertainer in the boxes on the home page (balloon shows, balloon twisting, balloon workshops, theatre shows (the three little balloon pigs on his head)
Nice to have
Should not have
• Element to avoid
• Stock imagery of balloon sculptures - use images provided.

```html
<!DOCTYPE html>
<html lang="en">
<head>
<meta charset="utf-8">
<title>Benny The Giggler – Children's Entertainer</title>
<link href="https://fonts.googleapis.com/css2?family=Open+Sans:wght@400;600;700&display=swap" rel="stylesheet">
<style>
:root{
  --blue:#34a6d7;
  --blue-light:#e6f4fb;
  --orange:#f37122;
  --navy:#26398f;
  --navy-deep:#1b2a6e;
  --dark:#1f2328;
  --darker:#141619;
  --text:#5a5f66;
  --white:#ffffff;
}
*{box-sizing:border-box;margin:0;padding:0}
html,body{width:847px;height:1200px;overflow:hidden;background:var(--white)}
body{font-family:'Open Sans',Arial,sans-serif;color:var(--text);position:relative}
.abs{position:absolute}

/* hero */
.hero{left:0;top:0;width:847px;height:466px;background:linear-gradient(90deg,var(--navy-deep) 0%,var(--navy) 40%,#3d5bb0 100%)}
.hero-photo{left:330px;top:0;width:517px;height:466px;background:radial-gradient(circle at 55% 45%,#e8c8a8 0 8%,#c9d4ec 18%,#5b7bc9 45%,rgba(38,57,143,0) 75%)}
.topbar{right:60px;top:6px;display:flex;gap:28px;font-size:10px;color:var(--white)}
.topbar span{display:flex;align-items:center;gap:6px}
.nav{left:254px;top:34px;display:flex;gap:24px;font-size:10.5px;font-weight:600;color:var(--white)}
.nav .active{border-bottom:2px solid var(--white);padding-bottom:4px}
.logo{left:84px;top:0;width:156px;height:258px;background:var(--orange);display:flex;flex-direction:column;align-items:center;justify-content:flex-end;padding-bottom:24px;gap:8px}
.logo-mark{width:18px;height:18px;background:var(--white);border-radius:50%}
.logo-name{color:var(--white);font-weight:700;font-size:17px;text-align:center;line-height:1.15}
.hero-copy{left:90px;top:280px;width:240px;color:var(--white);font-size:15px;line-height:1.4}
.btn-outline{left:90px;top:366px;width:134px;height:28px;border:1px solid var(--white);color:var(--white);font-size:11px;display:flex;align-items:center;justify-content:center;letter-spacing:.5px}
.dots{left:90px;top:410px;display:flex;gap:7px}
.dots i{width:9px;height:9px;border-radius:50%;border:1px solid var(--white)}
.dots i:first-child{background:var(--white)}

/* testimonial */
.testimonial{left:90px;top:478px;width:400px;height:100px;display:flex;gap:18px}
.avatar{width:64px;height:64px;border-radius:50%;background:var(--orange);flex:none}
.testimonial p{font-size:10px;line-height:1.5;color:var(--orange);margin-top:6px}
.testimonial .who{font-size:9px;color:var(--text);margin-top:4px}
.slider-dots{left:440px;top:560px;display:flex;gap:5px}
.slider-dots i{width:7px;height:7px;border-radius:50%;background:var(--orange);opacity:.5}
.slider-dots i:first-child{opacity:1}
.contact-card{left:530px;top:484px;width:226px;height:72px;border:2px solid var(--blue);display:flex;flex-direction:column}
.contact-card .head{background:var(--blue);color:var(--white);font-size:11px;font-weight:600;padding:8px 12px;letter-spacing:.5px}
.contact-card .phone{color:var(--blue);font-size:20px;font-weight:700;padding:4px 12px}

/* welcome band */
.band{left:0;top:600px;width:847px;height:182px;background:linear-gradient(90deg,#3a3d42,#55504c 50%,#3a3d42)}
.welcome{left:90px;top:622px;width:340px;color:var(--white)}
h2{font-size:15px;font-weight:600;letter-spacing:.5px;margin-bottom:10px}
.welcome p,.newsletter p{font-size:9.5px;line-height:1.55;color:#d9dbde}
.btn-small{display:inline-block;margin-top:10px;border:1px solid var(--white);color:var(--white);font-size:9px;padding:4px 10px}
.newsletter{left:530px;top:622px;width:226px;color:var(--white)}
.newsletter input{display:block;width:226px;height:22px;margin-top:10px;border:none;padding:0 8px;font-size:9px;font-family:inherit}

/* service cards */
.cards{left:90px;top:806px;width:666px;display:flex;gap:8px}
.card{width:160.5px;height:200px;position:relative}
.card-photo{position:absolute;inset:0}
.card-label{position:absolute;left:0;right:0;bottom:0;height:52px;background:rgba(20,22,25,.82);color:var(--white);font-size:13px;font-weight:600;line-height:1.15;padding:9px 10px}
.card-label svg{position:absolute;right:8px;bottom:10px}

/* call to action */
.cta{left:90px;top:1030px;width:666px;height:66px;background:var(--blue-light);border:2px solid var(--blue);display:flex;align-items:center;padding:0 16px 0 48px;gap:18px}
.cta h3{color:var(--blue);font-size:17px;font-weight:600;letter-spacing:.5px;flex:1}
.cta .phone{background:var(--blue);color:var(--white);font-weight:700;font-size:15px;padding:10px 16px}
.cta .callback{border:1px solid var(--blue);color:var(--blue);font-size:11px;font-weight:600;padding:11px 14px}

/* footer */
.footer{left:0;top:1112px;width:847px;height:88px;background:var(--dark)}
.footer-nav{left:0;top:1124px;width:847px;display:flex;justify-content:center;gap:30px;font-size:9.5px;color:var(--white)}
.footer-base{left:0;top:1162px;width:847px;height:38px;background:var(--darker);display:flex;align-items:center;justify-content:space-between;padding:0 90px;font-size:9px;color:#9aa0a6}
.social{display:flex;gap:12px}
.social i{width:10px;height:10px;border-radius:50%;background:#c7cbd0}
</style>
</head>
<body>

<section class="hero abs">
  <div class="hero-photo abs" role="img" aria-label="Entertainer smiling beside colourful balloon sculptures"></div>
</section>

<div class="topbar abs">
  <span><svg width="11" height="8" viewBox="0 0 11 8"><rect x=".5" y=".5" width="10" height="7" fill="none" stroke="#fff"/><path d="M.5 .5l5 4 5-4" fill="none" stroke="#fff"/></svg>info@bennygiggler.com</span>
  <span><svg width="9" height="10" viewBox="0 0 9 10"><path d="M1 1h2l1 2.5-1.2.8a6 6 0 0 0 3 3l.8-1.2L9 7v2H8A7 7 0 0 1 1 2z" fill="#fff"/></svg>012 555 0147</span>
</div>

<nav class="nav abs">
  <span class="active">HOME</span><span>BALLOON SHOWS</span><span>BALLOON TWISTING</span><span>THEATRE</span><span>REVIEWS</span><span>CONTACT</span>
</nav>

<div class="logo abs">
  <span class="logo-mark"></span>
  <span class="logo-name">Benny<br>The Giggler</span>
</div>

<p class="hero-copy abs">Lorem ipsum dolor sit amet, ex vim quem primis. Quot suavitate moderatius ex usu. Ridens eleifend ei sed.</p>
<div class="btn-outline abs">BOOK NOW</div>
<div class="dots abs"><i></i><i></i></div>

<div class="testimonial abs">
  <div class="avatar" role="img" aria-label="Portrait of a happy parent"></div>
  <div>
    <p>Lorem ipsum dolor sit amet, ex vim quem primis. Quot suavitate moderatius ex usu. Ridens eleifend ei sed, solum clita eu nec. Ut est altera graeco, mel at natum assum.</p>
    <p class="who">Mrs. Lorem Ipsum</p>
  </div>
</div>
<div class="slider-dots abs"><i></i><i></i><i></i></div>

<div class="contact-card abs">
  <div class="head">CONTACT THE ENTERTAINER</div>
  <div class="phone">012 555 0147</div>
</div>

<section class="band abs" role="img" aria-label="Children laughing at a balloon party"></section>
<div class="welcome abs">
  <h2>WELCOME TO BENNY THE GIGGLER</h2>
  <p>Lorem ipsum dolor sit amet, ex vim quem primis. Quot suavitate moderatius ex usu. Ridens eleifend ei sed, solum clita eu nec. Ut est altera graeco, mel at natum assum dolorem. Nam ut legimus mentitum, pri eu vero feugiat tincidunt, et quo tollit.</p>
  <span class="btn-small">READ MORE</span>
</div>
<div class="newsletter abs">
  <h2>SIGN UP FOR NEWSLETTER</h2>
  <p>Lorem ipsum dolor sit amet, ex vim quem primis. Quot suavitate moderatius ex usu.</p>
  <input type="text" placeholder="Enter your email">
  <span class="btn-small">SUBSCRIBE</span>
</div>

<div class="cards abs">
  <div class="card"><div class="card-photo" role="img" aria-label="Entertainer with a giant blue balloon" style="background:linear-gradient(180deg,#c9372c,#2e7fc4 60%,#1e5fa0)"></div>
    <div class="card-label">BALLOON<br>SHOWS<svg width="14" height="14" viewBox="0 0 14 14"><circle cx="7" cy="7" r="6.5" fill="none" stroke="#fff"/><path d="M6 4l3 3-3 3" fill="none" stroke="#fff"/></svg></div></div>
  <div class="card"><div class="card-photo" role="img" aria-label="Children holding twisted balloon animals" style="background:linear-gradient(180deg,#8a7a6c,#b98a5f 55%,#6e5a4a)"></div>
    <div class="card-label">BALLOON<br>TWISTING<svg width="14" height="14" viewBox="0 0 14 14"><circle cx="7" cy="7" r="6.5" fill="none" stroke="#fff"/><path d="M6 4l3 3-3 3" fill="none" stroke="#fff"/></svg></div></div>
  <div class="card"><div class="card-photo" role="img" aria-label="Balloon workshop with colourful balloons" style="background:linear-gradient(180deg,#d8d3c6,#e0a63a 50%,#c2433a)"></div>
    <div class="card-label">BALLOON<br>WORKSHOPS<svg width="14" height="14" viewBox="0 0 14 14"><circle cx="7" cy="7" r="6.5" fill="none" stroke="#fff"/><path d="M6 4l3 3-3 3" fill="none" stroke="#fff"/></svg></div></div>
  <div class="card"><div class="card-photo" role="img" aria-label="Entertainer on stage with balloon pigs on his head" style="background:linear-gradient(180deg,#b3202a,#8c1a22 60%,#5e1218)"></div>
    <div class="card-label">THEATRE<br>SHOWS<svg width="14" height="14" viewBox="0 0 14 14"><circle cx="7" cy="7" r="6.5" fill="none" stroke="#fff"/><path d="M6 4l3 3-3 3" fill="none" stroke="#fff"/></svg></div></div>
</div>

<div class="cta abs">
  <h3>CONTACT THE ENTERTAINER</h3>
  <span class="phone">012 555 0147</span>
  <span class="callback">REQUEST A CALL BACK</span>
</div>

<footer class="footer abs"></footer>
<div class="footer-nav abs"><span>Home</span><span>Balloon Shows</span><span>Balloon Twisting</span><span>Theatre</span><span>Reviews</span><span>Contact</span></div>
<div class="footer-base abs">
  <span>© 2015 – Benny The Giggler | All Rights Reserved</span>
  <span class="social"><i></i><i></i><i></i></span>
</div>

</body>
</html>
```